Medida Certa - Working hours register App needs interface design

Medida Certa, a 1 million users Brazilian website focused on general calculations needs an interface to an App for registering the working hours of a housemaid, a nanny, a housekeeper or other domestic workers.
The final users should be mainly housewifes.
The wireframe of the pages is in the LarPonto_layout.xls file attached.
Logo is also available in the wireframe.
The interface should be optimized for Android on Orbita KX with a 5'' screen.
Target Market(s)
Females, educated, from 30 to 50 y.o.
Industry/Entity Type
Android
Look and feel
Each slider illustrates characteristics of the customer's brand and the style your logo design should communicate.

```html
<!DOCTYPE html>
<html lang="en">
<head>
<meta charset="utf-8">
<title>Medida Certa · LarPonto</title>
<link href="https://fonts.googleapis.com/css2?family=Ubuntu:wght@400;500;700&display=swap" rel="stylesheet">
<style>
  :root {
    --header-top: #4a4a4c;
    --header-bottom: #151516;
    --brand-red: #e3262b;
    --brand-red-dark: #b30f14;
    --page-bg: #ffffff;
    --card-bg: #f2f2f2;
    --card-border: #d8d8d8;
    --name-ink: #2e2e2e;
    --sub-ink: #8a8a8a;
    --btn-top: #fbfbfb;
    --btn-bottom: #dedede;
    --btn-border: #b9b9b9;
    --btn-ink: #2a2a2a;
    --track: #e2e2e2;
    --thumb-top: #f04848;
    --thumb-bottom: #c50a10;
    --white: #ffffff;
  }
  * { box-sizing: border-box; margin: 0; padding: 0; }
  html, body { width: 675px; height: 1200px; overflow: hidden; background: var(--page-bg); }
  body { font-family: "Ubuntu", sans-serif; }

  .screen {
    position: relative;
    width: 720px; height: 1280px;
    transform: scale(0.9375);
    transform-origin: 0 0;
    overflow: hidden;
    background: var(--page-bg);
  }

  /* Header */
  .app-header {
    position: absolute; left: 0; top: 0; width: 720px; height: 155px;
    background: linear-gradient(180deg, var(--header-top) 0%, #2c2c2e 50%, var(--header-bottom) 100%);
    box-shadow: 0 6px 14px rgba(0,0,0,0.35);
    z-index: 5;
  }
  .brand-square {
    position: absolute; left: 32px; top: 20px; width: 121px; height: 121px;
    border-radius: 10px;
    background: linear-gradient(180deg, var(--brand-red) 0%, var(--brand-red-dark) 100%);
  }
  .brand-name {
    position: absolute; left: 170px; top: 43px;
    color: var(--white); font-weight: 700; font-size: 31px; letter-spacing: 0.5px;
  }
  .brand-app {
    position: absolute; left: 170px; top: 82px;
    color: var(--white); font-weight: 400; font-size: 26px; letter-spacing: 0.5px;
  }
  .edit-action {
    position: absolute; left: 641px; top: 53px; width: 50px; height: 49px;
    border-radius: 8px;
    background: linear-gradient(180deg, #5c5c5e, #2a2a2c);
    border: 1px solid #111;
    box-shadow: inset 0 1px 0 rgba(255,255,255,0.25);
  }
  .edit-action svg { position: absolute; left: 9px; top: 9px; }

  /* Employee list */
  .employee-list { position: absolute; left: 30px; top: 106px; width: 644px; }
  .employee-card {
    position: relative; height: 145px; margin-bottom: 6px;
    background: var(--card-bg); border: 1px solid var(--card-border);
  }
  .employee-photo {
    position: absolute; left: 10px; top: 11px; width: 124px; height: 124px;
    border: 1px solid #333;
  }
  .employee-name {
    position: absolute; left: 152px; top: 12px;
    font-size: 36px; font-weight: 400; color: var(--name-ink);
    white-space: nowrap;
  }
  .employee-role {
    position: absolute; left: 153px; top: 58px;
    font-size: 25px; color: var(--sub-ink);
  }
  .card-button {
    position: absolute; top: 101px; width: 174px; height: 34px;
    border: 1px solid var(--btn-border); border-radius: 5px;
    background: linear-gradient(180deg, var(--btn-top), var(--btn-bottom));
    font-family: "Ubuntu", sans-serif; font-weight: 500; font-size: 18px; color: var(--btn-ink);
    display: flex; align-items: center; justify-content: center;
  }
  .card-button.punch { left: 150px; }
  .card-button.edit { left: 332px; }

  /* Scrollbar */
  .scroll-track {
    position: absolute; left: 686px; top: 170px; width: 12px; height: 1093px;
    border: 1px solid var(--track); border-radius: 6px; background: var(--white);
  }
  .scroll-thumb {
    position: absolute; left: 684px; top: 410px; width: 14px; height: 274px;
    border-radius: 7px;
    background: linear-gradient(180deg, var(--thumb-top), var(--thumb-bottom));
  }

  .bottom-fade {
    position: absolute; left: 0; bottom: 0; width: 720px; height: 60px;
    background: linear-gradient(180deg, rgba(255,255,255,0) 0%, rgba(255,255,255,0.95) 100%);
    z-index: 4;
  }
</style>
</head>
<body>
<div class="screen">
  <header class="app-header">
    <div class="brand-square"></div>
    <div class="brand-name">MEDIDA CERTA</div>
    <div class="brand-app">LAR PONTO</div>
    <div class="edit-action">
      <svg width="30" height="30" viewBox="0 0 30 30" aria-hidden="true">
        <path d="M6 24 L8 17 L20 5 L25 10 L13 22 Z" fill="none" stroke="#fff" stroke-width="2.2" stroke-linejoin="round"/>
        <path d="M8 17 L13 22" stroke="#fff" stroke-width="2"/>
        <path d="M17.5 7.5 L22.5 12.5" stroke="#fff" stroke-width="2"/>
      </svg>
    </div>
  </header>

  <main class="employee-list">
    <article class="employee-card">
      <div class="employee-photo" role="img" aria-label="Portrait photo of Kyla" style="background:linear-gradient(90deg,#2a211d 0%,#d9b3a3 45%,#c99886 60%,#2b221d 100%)"></div>
      <div class="employee-name">Kyla McEmployee</div>
      <div class="employee-role">Lorem Impsum</div>
      <div class="card-button punch">Punch In</div><div class="card-button edit">Edit</div>
    </article>
    <article class="employee-card">
      <div class="employee-photo" role="img" aria-label="Portrait photo of Mike" style="background:linear-gradient(180deg,#f4f1ec 0%,#caa07e 40%,#d9a07e 60%,#e0531f 85%)"></div>
      <div class="employee-name">Mike McEmployee</div>
      <div class="employee-role">Lorem Impsum</div>
      <div class="card-button punch">Punch In</div><div class="card-button edit">Edit</div>
    </article>
    <article class="employee-card">
      <div class="employee-photo" role="img" aria-label="Portrait photo of Sunny" style="background:linear-gradient(90deg,#8a5a32 0%,#dcb89c 40%,#dcb89c 60%,#8c5c36 100%)"></div>
      <div class="employee-name">Sunny McEmployee</div>
      <div class="employee-role">Lorem Impsum</div>
      <div class="card-button punch">Punch In</div><div class="card-button edit">Edit</div>
    </article>
    <article class="employee-card">
      <div class="employee-photo" role="img" aria-label="Portrait photo of Natasha" style="background:linear-gradient(180deg,#c7b99a 0%,#3b2a22 30%,#d8a98c 60%,#c9a98a 100%)"></div>
      <div class="employee-name">Natasha McEmployee</div>
      <div class="employee-role">Lorem Impsum</div>
      <div class="card-button punch">Punch In</div><div class="card-button edit">Edit</div>
    </article>
    <article class="employee-card">
      <div class="employee-photo" role="img" aria-label="Portrait photo of Chriss" style="background:linear-gradient(180deg,#d2d7d5 0%,#7a5a40 20%,#e0b69a 50%,#eef0ef 90%)"></div>
      <div class="employee-name">Chriss McEmployee</div>
      <div class="employee-role">Lorem Impsum</div>
      <div class="card-button punch">Punch In</div><div class="card-button edit">Edit</div>
    </article>
    <article class="employee-card">
      <div class="employee-photo" role="img" aria-label="Portrait photo of Kyla" style="background:linear-gradient(90deg,#2a211d 0%,#d9b3a3 45%,#c99886 60%,#2b221d 100%)"></div>
      <div class="employee-name">Kyla McEmployee</div>
      <div class="employee-role">Lorem Impsum</div>
      <div class="card-button punch">Punch In</div><div class="card-button edit">Edit</div>
    </article>
    <article class="employee-card">
      <div class="employee-photo" role="img" aria-label="Portrait photo of Mike" style="background:linear-gradient(180deg,#f4f1ec 0%,#caa07e 40%,#d9a07e 60%,#e0531f 85%)"></div>
      <div class="employee-name">Mike McEmployee</div>
      <div class="employee-role">Lorem Impsum</div>
      <div class="card-button punch">Punch In</div><div class="card-button edit">Edit</div>
    </article>
    <article class="employee-card">
      <div class="employee-photo" role="img" aria-label="Portrait photo of Sunny" style="background:linear-gradient(90deg,#8a5a32 0%,#dcb89c 40%,#dcb89c 60%,#8c5c36 100%)"></div>
      <div class="employee-name">Sunny McEmployee</div>
      <div class="employee-role">Lorem Impsum</div>
      <div class="card-button punch">Punch In</div><div class="card-button edit">Edit</div>
    </article>
  </main>

  <div class="scroll-track"></div>
  <div class="scroll-thumb"></div>
  <div class="bottom-fade"></div>
</div>
</body>
</html>
```